Design of machine exterior and promotion wall

Overview: The task includes the design of the Pennyvault promotional stand, compromising the exterior of the Pennyvault machine as well as the promotional wall that will be placed directly behind it.

Deliverable: Coherently designed, well layered and high resolution PSD / EPS files with appropriate bleed margin for the front of the promotion wall, the back of the promotion wall and the machine exterior. Preview picture of branded machine in front of branded wall.

Details can be found in the attached design brief.

```html
<!DOCTYPE html>
<html lang="en">
<head>
<meta charset="utf-8">
<title>Pennyvault – Promotion Wall Back</title>
<link rel="stylesheet" href="https://fonts.googleapis.com/css2?family=Bebas+Neue&display=swap">
<style>
  :root {
    --wall-gold: #d3a02e;
    --wall-white: #ffffff;
    --brand-gold: #c4952f;
    --ink-dark: #4a4a4c;
    --art-dark: #2a2a2a;
    --art-mid: #3c3c3c;
  }
  * { margin: 0; padding: 0; box-sizing: border-box; }
  html, body {
    width: 1200px;
    height: 1152px;
    overflow: hidden;
    background: var(--wall-white);
  }
  .promo-wall {
    position: relative;
    width: 1200px;
    height: 1152px;
    overflow: hidden;
    font-family: "Bebas Neue", "Arial Narrow", sans-serif;
  }
  .wall-swoosh {
    position: absolute;
    inset: 0;
    width: 1200px;
    height: 1152px;
  }
  .brand-name {
    position: absolute;
    left: 90px;
    top: 110px;
    font-size: 84px;
    line-height: 1;
    letter-spacing: 2px;
    color: var(--brand-gold);
  }
  .how-it-works-art {
    position: absolute;
    left: 640px;
    top: 150px;
    width: 500px;
    height: 420px;
    border-radius: 6px;
    background: linear-gradient(160deg, var(--art-mid), var(--art-dark));
  }
  .headline {
    position: absolute;
    left: 100px;
    top: 600px;
    font-size: 122px;
    line-height: 0.95;
    color: var(--wall-white);
    white-space: nowrap;
    font-weight: 400;
  }
  .offer-text {
    position: absolute;
    left: 108px;
    top: 850px;
    font-size: 66px;
    line-height: 1.08;
    color: var(--ink-dark);
    white-space: nowrap;
  }
</style>
</head>
<body>
  <main class="promo-wall">
    <svg class="wall-swoosh" viewBox="0 0 1200 1152" aria-hidden="true">
      <rect width="1200" height="1152" fill="var(--wall-white)"/>
      <path d="M0,330 C420,330 880,200 1200,50 L1200,210 C880,330 440,385 0,385 Z" fill="var(--wall-gold)"/>
      <path d="M0,440 C460,435 880,350 1200,265 L1200,1152 L0,1152 Z" fill="var(--wall-gold)"/>
    </svg>

    <div class="brand-name">Pennyvault</div>

    <div class="how-it-works-art" role="img"
         aria-label="Illustration of a traveller inserting foreign coins into the Pennyvault machine and receiving a voucher"></div>

    <h1 class="headline">Don't get stuck with coins<br>you can't spend...</h1>

    <p class="offer-text">Turn your change into a voucher<br>to be redeemed against your purchase<br>at any Tarvo store in this airport.</p>
  </main>
</body>
</html>
```